Visitenkarten
Zielgruppe
Wir begleiten dich in der Ausbildung, im Studium, bei der Fachwirt-Weiterbildung, damit du deine Prüfungen ohne Hindernisse erfolgreich meisterst.
Aufgabenstellung
Auf der Visitenkarte muss das Logo und folgende Informationen zu sehen sein:
Lernwerkcoach
Timo Brandau
Quaderweg Str. 58
04388 Leipzig
Telefon: 0152 - 3208947
E-Mail: info@lernwerkcoach-beispiel.de
Homepage: www.lernwerkcoach-beispiel.de
sowie einen Link zu meinem Terminvereinbarungskalender: www.terminfix-beispiel.de/lernwerkcoach mit dem Hinweis: „Hier Termin vereinbaren“ (sinngemäße Abwandlung möglich).
Es muss auch ein Hinweis auf eine kostenfreie Probestunde drauf.

```html
<!DOCTYPE html>
<html lang="de">
<head>
<meta charset="utf-8">
<title>Lernwerkcoach – Visitenkarte</title>
<link rel="stylesheet" href="https://fonts.googleapis.com/css2?family=Arimo:wght@400;700&display=swap">
<style>
  :root{
    --teal:#1c4c51;
    --teal-dark:#163f43;
    --teal-soft:#2b6166;
    --ink:#1f4a4f;
    --muted:#6f8c8f;
    --paper:#ffffff;
    --stage:#e6e8e8;
  }
  *{box-sizing:border-box;margin:0;padding:0}
  html,body{width:1200px;height:901px;overflow:hidden}
  body{background:var(--stage);font-family:"Arimo",Arial,sans-serif;position:relative}

  .card{position:absolute;width:540px;height:309px;box-shadow:0 10px 28px rgba(0,0,0,.22)}

  /* back side */
  .card-back{left:60px;top:110px;background:var(--teal);overflow:hidden}
  .back-pattern{position:absolute;inset:0;
    background:radial-gradient(circle at 50% 50%,var(--teal-soft) 0%,var(--teal) 55%,var(--teal-dark) 100%)}
  .back-name{position:absolute;left:0;right:0;top:138px;text-align:center;
    color:var(--paper);font-weight:700;font-size:22px;letter-spacing:.5px}

  /* front side */
  .card-front{left:600px;top:480px;background:var(--paper);overflow:hidden}
  .front-band{position:absolute;left:0;right:0;bottom:0;height:9px;background:var(--teal)}

  .brand{position:absolute;left:28px;top:28px;display:flex;align-items:center;gap:14px}
  .brand-square{width:44px;height:44px;background:var(--teal)}
  .brand-divider{width:1px;height:56px;background:var(--ink)}
  .brand-name{font-weight:700;font-size:30px;color:var(--ink);line-height:1}
  .brand-tagline{font-size:7.2px;font-weight:700;letter-spacing:.6px;color:var(--ink);margin-top:5px;line-height:1.25}

  .person{position:absolute;left:30px;top:118px}
  .person-name{font-weight:700;font-size:20px;color:var(--ink)}
  .person-role{font-size:14px;color:var(--muted);margin-top:2px}

  .address{position:absolute;left:30px;top:178px;font-size:12.5px;color:var(--muted);line-height:1.45}

  .contact{position:absolute;left:30px;top:230px;list-style:none;font-size:12.5px;color:var(--muted)}
  .contact li{display:flex;align-items:center;gap:9px;height:20px}
  .contact svg{width:14px;height:14px;fill:none;stroke:var(--ink);stroke-width:1.6}

  .booking{position:absolute;right:26px;top:104px;width:240px;height:112px;
    border:2px solid var(--ink);border-radius:14px;text-align:center;color:var(--ink)}
  .booking-label{font-size:13.5px;margin-top:38px}
  .booking-rule{height:2px;background:var(--ink);margin:10px 0 8px}
  .booking-url{font-size:11.5px;color:var(--muted)}

  .trial{position:absolute;right:26px;top:232px;width:240px;text-align:center;font-size:12.5px;color:var(--muted)}
</style>
</head>
<body>

<section class="card card-back" aria-label="Rückseite">
  <div class="back-pattern" role="img" aria-label="Fläche mit wiederholtem Bildmuster in Petrol"></div>
  <p class="back-name">Lernwerkcoach</p>
</section>

<section class="card card-front" aria-label="Vorderseite">
  <div class="brand">
    <span class="brand-square"></span>
    <span class="brand-divider"></span>
    <div>
      <p class="brand-name">Lernwerkcoach</p>
      <p class="brand-tagline">WEITERBILDUNGSINSTITUT FÜR RECHNUNGSWESEN,<br>WIRTSCHAFTSLEHRE UND STEUERRECHT</p>
    </div>
  </div>

  <div class="person">
    <p class="person-name">Timo Brandau</p>
    <p class="person-role">Lernwerkcoach</p>
  </div>

  <p class="address">Quaderweg Str. 58<br>04388 Leipzig</p>

  <ul class="contact">
    <li><svg viewBox="0 0 16 16"><path d="M3 2h3l1.5 3.5-2 1.2a8 8 0 0 0 3.8 3.8l1.2-2L14 10v3a1 1 0 0 1-1 1A11 11 0 0 1 2 3a1 1 0 0 1 1-1z"/></svg>0152 - 3208947</li>
    <li><svg viewBox="0 0 16 16"><rect x="1.5" y="3.5" width="13" height="9"/><path d="M1.5 3.5 8 9l6.5-5.5"/></svg>info@lernwerkcoach-beispiel.de</li>
    <li><svg viewBox="0 0 16 16"><circle cx="8" cy="8" r="6.5"/><path d="M1.5 8h13M8 1.5c2.2 2 2.2 11 0 13M8 1.5c-2.2 2-2.2 11 0 13"/></svg>www.lernwerkcoach-beispiel.de</li>
  </ul>

  <div class="booking">
    <p class="booking-label">Hier Termin vereinbaren:</p>
    <div class="booking-rule"></div>
    <p class="booking-url">www.terminfix-beispiel.de/lernwerkcoach</p>
  </div>

  <p class="trial">eine kostenfreie Probestunde drauf</p>

  <div class="front-band"></div>
</section>

</body>
</html>
```